Web Design Project - Homepage mockup for media services company

Client would like a site much like this example below in terms of design and layout:

http://fernquill.net/

It's a media services company and the services they provide are:
-audio/video production
-graphic design
-social media
-web development
-apparel design

Their logo file is attached. I have also attached some of their service descriptions if that at all helps with things.

```html
<!DOCTYPE html>
<html lang="en">
<head>
<meta charset="utf-8">
<title>Veloria Media — Home</title>
<link href="https://fonts.googleapis.com/css2?family=Oswald:wght@300;400&family=Open+Sans:wght@400;600&display=swap" rel="stylesheet">
<style>
:root{
  --ink:#222;
  --dark:#3b3b3b;
  --darker:#2f2f2f;
  --panel:#f0f0f0;
  --line:#d6d6d6;
  --text:#444;
  --white:#fff;
  --muted:#6a6a6a;
}
*{margin:0;padding:0;box-sizing:border-box}
html,body{width:900px;height:1200px;overflow:hidden;background:var(--white)}
body{position:relative;font-family:"Open Sans",Arial,sans-serif;color:var(--text)}
.abs{position:absolute}

/* header */
.site-header{left:0;top:0;width:900px;height:82px;background:var(--white)}
.brand{left:68px;top:6px;display:flex;align-items:center;gap:8px}
.brand-mark{width:66px;height:66px;border-radius:50%;background:var(--darker)}
.brand-name{font-family:"Oswald",sans-serif;font-weight:400;font-size:26px;color:var(--ink)}
.main-nav{left:273px;top:0;height:82px;display:flex}
.main-nav a{display:flex;align-items:center;height:82px;padding:0 16px;font-size:11px;color:#333;text-decoration:none;letter-spacing:.2px}
.main-nav a.current{background:var(--dark);color:var(--white);padding:0 14px}

/* hero */
.hero{left:0;top:82px;width:900px;height:336px;
  background:radial-gradient(circle at 80% 20%,#bfe9f5 0,#3fb6dc 25%,transparent 55%),
  linear-gradient(115deg,#1d3f6a 0%,#5a2b8a 25%,#d93a8f 42%,#f4c21f 58%,#e0352a 70%,#2a6fb0 85%,#0f2d58 100%)}
.hero-arrow{top:212px;width:20px;height:40px}
.hero-caption{left:65px;top:337px;width:769px;height:61px;background:rgba(50,50,50,.92);display:flex}
.hero-title{flex:1;font-family:"Oswald",sans-serif;font-size:23px;color:var(--white);line-height:61px;padding-left:19px}
.hero-dots{width:140px;background:rgba(40,40,40,.95);display:flex;align-items:center;justify-content:center;gap:8px}
.hero-dots span{width:14px;height:14px;border-radius:50%;background:#222;box-shadow:inset 0 1px 2px #000}
.hero-dots span.on{background:#ddd}

/* service cards */
.card{top:446px;width:148px;height:210px;border:1px solid var(--line);background:linear-gradient(#fff 60%,#ece7ea)}
.card h3{height:38px;background:var(--dark);color:var(--white);font-family:"Oswald",sans-serif;font-weight:400;font-size:18px;line-height:38px;padding-left:15px;white-space:nowrap}
.card .thumb{margin:15px 0 0 15px;width:124px;height:67px;box-shadow:0 1px 3px rgba(0,0,0,.4)}
.card p{margin:15px 12px 0 15px;font-family:Arial,sans-serif;font-size:9.3px;line-height:13.5px;color:#555}
.card .plus{position:absolute;left:66px;bottom:-7px;width:14px;height:14px;background:#333;color:#fff;font-size:11px;line-height:13px;text-align:center}

/* info band */
.info{left:0;top:685px;width:900px;height:241px;background:var(--panel)}
.col-rule{top:685px;width:1px;height:241px;background:#ddd}
.col-head{display:flex;align-items:center;gap:10px}
.col-icon{width:34px;height:34px;border-radius:50%;background:#444;display:flex;align-items:center;justify-content:center}
.col-head h2{font-family:"Oswald",sans-serif;font-weight:400;font-size:18px;color:#333}
.svc-list{list-style:none;font-family:Arial,sans-serif;font-size:10.5px;color:#222}
.svc-list li{height:22.4px;display:flex;align-items:center;gap:9px}
.entry h4{font-weight:400;font-size:12px;color:#333;margin-bottom:8px}
.entry p{font-size:9px;line-height:10.5px;color:#333}
.more{width:51px;height:20px;border-radius:7px;background:#1e1e1e;color:#fff;font-size:8.5px;font-weight:600;text-align:center;line-height:20px;box-shadow:0 1px 2px #000}

/* footer */
.site-footer{left:0;top:926px;width:900px;height:274px;background:var(--dark)}
.foot-title{font-family:"Oswald",sans-serif;font-weight:300;font-size:27px;color:var(--white);text-align:center}
.quick-links{list-style:none;text-align:center;font-size:10px;color:#eee;letter-spacing:.3px}
.quick-links li{height:19.5px}
.field{left:335px;width:228px;height:29px;border-radius:10px;background:var(--white);font-size:9px;color:#333;padding:8px 14px}
.submit{left:424px;top:1138px;width:52px;height:20px;border-radius:7px;background:#1e1e1e;border:1px solid #666;color:#fff;font-size:8.5px;font-weight:600;text-align:center;line-height:18px}
.address{text-align:center;color:#eee;font-size:8px;line-height:15px}
.address strong{display:block;font-weight:400;font-size:11.5px;margin-bottom:2px}
.social{top:1137px;width:32px;height:32px;border-radius:50%;background:#575757;box-shadow:inset 0 1px 2px #222}
.copyright{left:68px;top:1165px;font-family:Arial,sans-serif;font-size:9.5px;color:#eee}
.foot-edge{left:0;top:1194px;width:900px;height:6px;background:#6a6a6a}
</style>
</head>
<body>

<header class="abs site-header">
  <div class="abs brand"><span class="brand-mark"></span><span class="brand-name">Veloria Media</span></div>
  <nav class="abs main-nav">
    <a class="current">HOME</a><a>ABOUT US</a><a>SERVICES</a><a>GALLERY</a><a>BLOG</a><a>TESTIMONIALS</a><a>CONTACT US</a>
  </nav>
</header>

<section class="abs hero" role="img" aria-label="Flowing rainbow ribbon against a soft blue bokeh background"></section>
<svg class="abs hero-arrow" style="left:22px" viewBox="0 0 20 40"><path d="M16 8 L5 20 L16 32" fill="none" stroke="#fff" stroke-width="2"/></svg>
<svg class="abs hero-arrow" style="left:858px" viewBox="0 0 20 40"><path d="M4 8 L15 20 L4 32" fill="none" stroke="#fff" stroke-width="2"/></svg>
<div class="abs hero-caption">
  <div class="hero-title">HEADING TITLE LINE COMES HERE</div>
  <div class="hero-dots"><span class="on"></span><span></span><span></span><span></span><span></span></div>
</div>

<article class="abs card" style="left:65px">
  <h3>AUDIO / VIDEO</h3>
  <div class="thumb" role="img" aria-label="Audio and video media player illustration" style="background:linear-gradient(135deg,#1a1a1a,#3a4a6a 50%,#111)"></div>
  <p>When something is lacking excellent audio it is the first thing the listener notices...</p>
  <span class="plus">+</span>
</article>
<article class="abs card" style="left:220px">
  <h3>GRAPHIC DESIGN</h3>
  <div class="thumb" role="img" aria-label="Colourful abstract floral graphic artwork" style="background:linear-gradient(120deg,#1e6fc0,#f2c21a 40%,#e2367a 65%,#3aa34a)"></div>
  <p>Being one of the most powerful tools for enhancing your companies image...</p>
  <span class="plus">+</span>
</article>
<article class="abs card" style="left:375px">
  <h3>SOCIAL MEDIA</h3>
  <div class="thumb" role="img" aria-label="Social media icons on teal background" style="background:linear-gradient(135deg,#0d3b44,#1c7f86 60%,#0b2e36)"></div>
  <p>When executed correctly, social media can evolve your business...</p>
  <span class="plus">+</span>
</article>
<article class="abs card" style="left:530px">
  <h3>WEB DEVELOPMENT</h3>
  <div class="thumb" role="img" aria-label="Web development concept with globe" style="background:linear-gradient(135deg,#dfe6ef,#f5f5f5 50%,#3a6fb5)"></div>
  <p>Being one of the most powerful tools for enhancing your companies image...</p>
  <span class="plus">+</span>
</article>
<article class="abs card" style="left:685px">
  <h3>APPAREL DESIGN</h3>
  <div class="thumb" role="img" aria-label="Ornamental sun print artwork" style="background:radial-gradient(circle,#f0c860,#c9a24a 60%,#a8893e)"></div>
  <p>We recognize what stands out when it comes to framing a photo...</p>
  <span class="plus">+</span>
</article>

<section class="abs info"></section>
<div class="abs col-rule" style="left:315px"></div>
<div class="abs col-rule" style="left:587px"></div>

<div class="abs col-head" style="left:67px;top:699px">
  <span class="col-icon"><svg width="18" height="14" viewBox="0 0 18 14"><path d="M3 7V4h10l-2-2M15 7v3H5l2 2" fill="none" stroke="#fff" stroke-width="2"/></svg></span>
  <h2>SERVICES</h2>
</div>
<ul class="abs svc-list" style="left:94px;top:742px">
  <li><svg width="10" height="8"><path d="M0 3h5V0l5 4-5 4V5H0z" fill="#222"/></svg>Audio / Video production</li>
  <li><svg width="10" height="8"><path d="M0 3h5V0l5 4-5 4V5H0z" fill="#222"/></svg>Graphic design</li>
  <li><svg width="10" height="8"><path d="M0 3h5V0l5 4-5 4V5H0z" fill="#222"/></svg>Social media</li>
  <li><svg width="10" height="8"><path d="M0 3h5V0l5 4-5 4V5H0z" fill="#222"/></svg>Web development</li>
  <li><svg width="10" height="8"><path d="M0 3h5V0l5 4-5 4V5H0z" fill="#222"/></svg>Apparel design</li>
</ul>
<div class="abs more" style="left:255px;top:888px">MORE</div>

<div class="abs col-head" style="left:336px;top:699px">
  <span class="col-icon"><svg width="16" height="16" viewBox="0 0 16 16"><circle cx="8" cy="5" r="3.5" fill="#fff"/><path d="M1 16c0-5 3-7 7-7s7 2 7 7z" fill="#fff"/></svg></span>
  <h2>TESTIMONIALS</h2>
</div>
<div class="abs entry" style="left:340px;top:749px;width:240px">
  <h4>Title Headline Comes Here</h4>
  <p>Sed ut perspiciatis unde omnis iste natus error sit voluptatem accusantium doloremque error sit voluptatem accusantium doloremque</p>
</div>
<div class="abs entry" style="left:340px;top:824px;width:240px">
  <h4>Title Headline Comes Here</h4>
  <p>Sed ut perspiciatis unde omnis iste natus error sit voluptatem accusantium doloremque error sit voluptatem accusantium doloremque</p>
</div>
<div class="abs more" style="left:526px;top:888px">MORE</div>

<div class="abs col-head" style="left:614px;top:699px">
  <span class="col-icon"><svg width="16" height="16" viewBox="0 0 16 16"><path d="M2 14C4 6 9 3 15 2c-1 6-5 10-11 10" fill="#fff"/></svg></span>
  <h2>LATEST NEWS</h2>
</div>
<div class="abs entry" style="left:617px;top:749px;width:220px">
  <h4>Title Headline Comes Here</h4>
  <p>Nemo enim ipsam voluptatem quia voluptas sit aspernatur aut odit aut fugit, sed quia magni dolores eos qui ratione voluptatem sequi nesciunt.</p>
  <p style="margin-top:10px">Neque porro quisquam est, qui dolorem ipsum quia dolor sit amet, consectetur, adipisci velit, sed quia non numquam eius modi tempora incidunt ut labore et dolore magnam aliquam quaerat voluptatem.</p>
</div>
<div class="abs more" style="left:784px;top:888px">MORE</div>

<footer class="abs site-footer"></footer>
<div class="abs col-rule" style="left:318px;top:926px;height:274px;background:#2e2e2e"></div>
<div class="abs col-rule" style="left:584px;top:926px;height:274px;background:#2e2e2e"></div>

<h2 class="abs foot-title" style="left:90px;top:955px;width:200px">Quick Links</h2>
<ul class="abs quick-links" style="left:110px;top:1003px;width:160px">
  <li>HOME</li><li>ABOUT US</li><li>SERVICES</li><li>GALLERY</li><li>BLOG</li><li>TESTIMONIALS</li><li>CONTACT US</li>
</ul>

<h2 class="abs foot-title" style="left:350px;top:955px;width:200px">Quick Contact</h2>
<div class="abs field" style="top:1003px">Name</div>
<div class="abs field" style="top:1040px">Email</div>
<div class="abs field" style="top:1078px;height:45px">Message</div>
<div class="abs submit">SUBMIT</div>

<h2 class="abs foot-title" style="left:613px;top:955px;width:200px">Contact Us Today</h2>
<div class="abs address" style="left:630px;top:1000px;width:170px">
  <strong>Address</strong>
  Lorem Lipsum<br>Street Name,<br>City Name,<br>Pincode.<br>Phone: 123 456 7890<br>Fax: 123 456 7890<br>info@website.com
</div>
<span class="abs social" style="left:634px"></span>
<span class="abs social" style="left:677px"></span>
<span class="abs social" style="left:720px"></span>
<span class="abs social" style="left:762px"></span>

<p class="abs copyright">Copyrights © 2013. All Rights Reserved.</p>
<div class="abs foot-edge"></div>

</body>
</html>
```